Executive Performance Review mapped on J-curve

I need to turn an executive company performance review into a visual infographic. The list of accomplishments is grouped into four calendar quarters. Each quarter needs a subtle representation of the season. The four quarters and associated list of accomplishments need to be mapped to a J-curve. - Spreadsheet with accomplishments attached (Throughput)- Sample image of a J-curve. You can google J-curve to see more images.- The title should be "Danela Morsky Year in Review"

Target Market(s)

Board of Directors

Requirements
Nice to have
• This will be presented to a company founder that is an artist and customer experience expert. He is very visual so a nice visual representation of the data will be impactful. He also uses the phrase that you have to live with or work with someone for four seasons before you really know them. This is why I have the seasons mapped to the quarters. The Fall season motif should be gloomy and stormy.

```html
<!DOCTYPE html>
<html lang="en">
<head>
<meta charset="utf-8">
<title>Danela Morsky Year in Review</title>
<link rel="stylesheet" href="https://fonts.googleapis.com/css2?family=Open+Sans:wght@400;600;700;800&family=Courgette&display=swap">
<style>
:root{
  --bg:#0f3540;
  --label:#e6e6e6;
  --label-alt:#d8d8d8;
  --ink:#222;
  --summer-cell:#dfe7dd;
  --summer-cell-alt:#cfdccc;
  --fall-cell:#f0ddd6;
  --fall-cell-alt:#dfcbc0;
  --winter-cell:#e2e9ee;
  --winter-cell-alt:#d2dde3;
  --spring-cell:#eef0e0;
  --spring-cell-alt:#dde2c9;
  --summer:#2c7a2b;
  --fall:#f0360e;
  --winter:#5ba4bc;
  --spring:#4e8f23;
  --curve:#454545;
}
*{box-sizing:border-box;margin:0;padding:0}
html,body{width:678px;height:1200px;overflow:hidden}
body{background:var(--bg);font-family:"Open Sans",sans-serif;color:var(--ink);position:relative}
.title{position:absolute;left:18px;top:16px;color:#fff}
.title__name{font-weight:800;font-size:38px;line-height:40px}
.title__rule{width:157px;height:2px;background:#fff;margin:7px 0 6px}
.title__sub{font-weight:700;font-size:20px}
.journey{position:absolute;left:0;top:0}
.season-label{position:absolute;color:#fff;text-align:right;line-height:1}
.season-label__name{font-family:"Courgette",cursive;font-size:22px}
.season-label__quarter{font-weight:700;font-size:9px;display:block;margin-top:1px}
.review{position:absolute;left:17px;width:645px;display:grid;grid-template-columns:147px 249px 249px}
.review--first{top:256px;grid-template-rows:48px 70px 124px 69px 70px 69px 24px}
.review--second{top:746px;grid-template-rows:49px 70px 91px 70px 68px 70px 26px}
.cell{font-size:8px;line-height:11.5px;display:flex;align-items:center;padding:0 8px}
.cell--label{background:var(--label);justify-content:center;text-align:center;font-weight:700;font-size:10px;line-height:14px}
.cell--label.alt{background:var(--label-alt)}
.summer{background:var(--summer-cell)} .summer.alt{background:var(--summer-cell-alt)}
.fall{background:var(--fall-cell)} .fall.alt{background:var(--fall-cell-alt)}
.winter{background:var(--winter-cell)} .winter.alt{background:var(--winter-cell-alt)}
.spring{background:var(--spring-cell)} .spring.alt{background:var(--spring-cell-alt)}
.list{list-style:none}
.list li{position:relative;padding-left:12px}
.list li::before{content:"";position:absolute;left:1px;top:4px;width:4px;height:4px;border-radius:50%;background:currentColor}
.summer .list li::before{background:var(--summer)}
.fall .list li::before{background:var(--fall)}
.winter .list li::before{background:var(--winter)}
.spring .list li::before{background:var(--spring)}
.tbd{padding-left:20px}
.season-head{position:relative;display:flex;align-items:center;justify-content:space-between;padding:0 8px 0 10px;overflow:hidden}
.season-head__name{font-family:"Courgette",cursive;font-size:36px;line-height:1;position:relative}
.season-head__meta{font-weight:700;font-size:12px;line-height:14px;text-align:right;position:relative}
.head-summer{background:linear-gradient(100deg,#2d8a22,#6fbf3a 45%,#3b9a2a 75%,#1e6d1c)}
.head-summer .season-head__name{color:#1b3ea6}
.head-summer .season-head__meta{color:#1b5fb0}
.head-fall{background:linear-gradient(100deg,#f07d12,#f6b032 40%,#ef6a12 75%,#e24a0c)}
.head-fall .season-head__name{color:#8b0d0d}
.head-fall .season-head__meta{color:#8b0d0d}
.head-winter{background:linear-gradient(100deg,#cfe6f2,#ffffff 45%,#d9edf6 75%,#b8dbeb)}
.head-winter .season-head__name{color:#1a6f90}
.head-winter .season-head__meta{color:#1a6f90}
.head-spring{background:linear-gradient(100deg,#e9efb0,#f7f6d6 40%,#cfe38a 75%,#a8cf5a)}
.head-spring .season-head__name{color:#2f5f0c}
.head-spring .season-head__meta{color:#4a7f14}
.effect{font-weight:700;font-size:13px;color:#fff;display:flex;align-items:center;padding-left:18px}
.effect--summer{background:var(--summer)}
.effect--fall{background:var(--fall)}
.effect--winter{background:var(--winter)}
.effect--spring{background:var(--spring)}
</style>
</head>
<body>

<header class="title">
  <div class="title__name">Danela<br>Morsky</div>
  <div class="title__rule"></div>
  <div class="title__sub">Year in Review</div>
</header>

<svg class="journey" width="678" height="240" viewBox="0 0 678 240" aria-hidden="true">
  <path d="M353 149 C368 163 378 180 394 178 C416 175 480 116 506 90 C526 70 540 46 548 32" fill="none" stroke="var(--curve)" stroke-width="7" stroke-linecap="round"/>
  <g>
    <circle cx="353" cy="149" r="9" fill="#fff" stroke="#3b9a2a" stroke-width="4"/>
    <circle cx="353" cy="149" r="3.5" fill="#2c7a2b"/>
    <circle cx="394" cy="178" r="9" fill="#fff" stroke="#f0360e" stroke-width="4"/>
    <circle cx="394" cy="178" r="3.5" fill="#f0360e"/>
    <circle cx="506" cy="90" r="9" fill="#fff" stroke="#5ba4bc" stroke-width="4"/>
    <circle cx="506" cy="90" r="3.5" fill="#5ba4bc"/>
    <circle cx="548" cy="32" r="9" fill="#fff" stroke="#8cc43f" stroke-width="4"/>
    <circle cx="548" cy="32" r="3.5" fill="#4e8f23"/>
  </g>
</svg>

<div class="season-label" style="left:250px;top:134px;width:82px">
  <span class="season-label__name">Summer</span><span class="season-label__quarter" style="text-align:center;margin-right:12px">Q3 2018</span>
</div>
<div class="season-label" style="left:366px;top:194px;width:58px;text-align:center">
  <span class="season-label__name">Fall</span><span class="season-label__quarter">Q4 2018</span>
</div>
<div class="season-label" style="left:530px;top:80px;text-align:left">
  <span class="season-label__name">Winter</span><span class="season-label__quarter" style="margin-left:14px">Q1 2019</span>
</div>
<div class="season-label" style="left:571px;top:20px;text-align:left">
  <span class="season-label__name">Spring</span><span class="season-label__quarter" style="margin-left:12px">Q2 2019</span>
</div>

<section class="review review--first">
  <div class="cell cell--label"></div>
  <div class="season-head head-summer" role="img" aria-label="Summer foliage banner in bright greens">
    <span class="season-head__name">Summer</span><span class="season-head__meta">Q3 2018<br>Assessment</span>
  </div>
  <div class="season-head head-fall" role="img" aria-label="Autumn leaves banner in stormy oranges">
    <span class="season-head__name">Fall</span><span class="season-head__meta">Q4 2018<br>Stablize</span>
  </div>

  <div class="cell cell--label">Season<br>Transitions</div>
  <div class="cell summer"><ul class="list">
    <li>RO Transition from Reid &amp; Mira</li><li>Start CR Office Initiative</li><li>Tactical Ops transition from Reid</li><li>Formalize Exec Team</li></ul></div>
  <div class="cell fall"></div>

  <div class="cell cell--label alt">Biz Architecture</div>
  <div class="cell summer alt"><ul class="list">
    <li>Independent Financial Audit</li><li>Organizational Audit - Structure</li><li>Organizational Audit - People</li><li>XF Framework - ESU</li><li>Defined Utilization, Realization, Availability</li></ul></div>
  <div class="cell fall alt"><ul class="list">
    <li>XF Framework - Functional Meetings &amp; Scrum of Scrums</li><li>Structured Reorg</li><li>Implemented Reorg</li><li>Quarterly Org Iteration cadence</li><li>Defined Key Hire Plan</li><li>CR Office Operational</li><li>Time Accountability</li><li>Tools ReConfig</li><li>Org Structure v1</li></ul></div>

  <div class="cell cell--label">Strategy</div>
  <div class="cell summer"><ul class="list">
    <li>Effective Strategy Meeting</li><li>Strategic Themes 2018 - 2020: Stablize, Accelerate, Surge</li><li>Business Drivers: Drive Revenue, Improve Quellora</li><li>Experience, Increase Brand Awareness</li></ul></div>
  <div class="cell fall"><ul class="list"><li>Internal QBR Accountability</li></ul></div>

  <div class="cell cell--label alt">Sales</div>
  <div class="cell summer alt"><ul class="list">
    <li>Harwell Account Transition</li><li>QNT Account Transition</li><li>2 year Managed Services Engagement Model</li></ul></div>
  <div class="cell fall alt"><ul class="list"><li>Lantern QBR</li><li>Harwell QBR</li></ul></div>

  <div class="cell cell--label">Revenue / EBITA</div>
  <div class="cell summer"><span class="tbd">TBD</span></div>
  <div class="cell fall"><span class="tbd">TBD</span></div>

  <div class="cell cell--label alt">Effectiveness</div>
  <div class="effect effect--summer">Storming</div>
  <div class="effect effect--fall">Activity</div>
</section>

<section class="review review--second">
  <div class="cell cell--label">Season</div>
  <div class="season-head head-winter" role="img" aria-label="Winter snowflake banner in icy blues">
    <span class="season-head__name">Winter</span><span class="season-head__meta">Q1 2019<br>Stratactical</span>
  </div>
  <div class="season-head head-spring" role="img" aria-label="Spring meadow banner in fresh greens">
    <span class="season-head__name">Spring</span><span class="season-head__meta">Q2 2019<br>Strategic</span>
  </div>

  <div class="cell cell--label alt">Biz Architecture</div>
  <div class="cell winter alt"><ul class="list">
    <li>XF Framework - Progress Demos</li><li>Org Structure - COE's</li><li>Stablize Accounting &amp; Finance</li><li>Exec Hiring Process</li></ul></div>
  <div class="cell spring alt"><ul class="list">
    <li>Tiered Pricing Pre-Paid Engagement Model</li><li>XF Framework - Ideation Board</li><li>Consulting Levels &amp; Salary Bands</li><li>Roles &amp; Responsibilities</li></ul></div>

  <div class="cell cell--label">Key Hires</div>
  <div class="cell winter"><ul class="list"><li>Controller</li><li>Director CX</li></ul></div>
  <div class="cell spring"><ul class="list">
    <li>Interim HR</li><li>Provisional Client Partner</li><li>Acting Director 1</li><li>Acting Director 2</li><li>Client Partner 1</li><li>Sales Exec 1</li></ul></div>

  <div class="cell cell--label alt">Strategy</div>
  <div class="cell winter alt"><ul class="list">
    <li>Founders removed from front line activity</li><li>Veranda QBR - Goal Setting &amp; Tracking</li></ul></div>
  <div class="cell spring alt"></div>

  <div class="cell cell--label">Sales</div>
  <div class="cell winter"><ul class="list"><li>QNT QBR</li><li>Harwell QBR</li></ul></div>
  <div class="cell spring"><ul class="list">
    <li>Opened BrightPane Door</li><li>Flipped focus from operationaly run company to sales /marketing driven org</li><li>KTR Direct</li></ul></div>

  <div class="cell cell--label alt">Revenue / EBITA</div>
  <div class="cell winter alt"><span class="tbd">TBD</span></div>
  <div class="cell spring alt"><span class="tbd">TBD</span></div>

  <div class="cell cell--label">Effectiveness</div>
  <div class="effect effect--winter">Throughput</div>
  <div class="effect effect--spring">Outcomes</div>
</section>

</body>
</html>
```